Brochure for services and brand overview of new agency

With the recent launch of a new brand and business strategy agency, I am looking for a 2-3 page digital brochure that I can attach to emails as I open the dialogue with potential clients. This brochure has to fall in line with our brand...modern and sleek, with a highly professional look and feel. The content can come from a combination of our website (www.quillbarn.co) and any additional content can come from you or just ask me to provide. Logos and other materials are provided as well. I have also included a sample of one of my other brochures from another company I own, just so you can get an example of the quality and feel I like.

Target Market(s)

Divorce Professionals (Attorneys, Mediators, Therapists, etc)

Industry/Entity Type

Agency

Font styles to use
Serif

Requirements
Must have
• High end brand feel.
Specific content with relation to services, brand ethos, etc....with a subtle call to action.
Should not have
• Hard Sales Language
Cheap looking stock photos

Don't go too heavy in written content. Just scratch the surface in a way that will capture attention and get them to want to call. It's more about the design and inspirational aspects of it.

```html
<!DOCTYPE html>
<html lang="en">
<head>
<meta charset="utf-8">
<title>Quillbarn Agency Brochure</title>
<link href="https://fonts.googleapis.com/css2?family=Montserrat:wght@300;400;500;600;700&display=swap" rel="stylesheet">
<style>
:root{
  --stage:#a9aaad;
  --ink:#111111;
  --black:#0c0c0d;
  --white:#ffffff;
  --red:#d01f37;
  --mist:#d9d9da;
  --office-a:#3b5a86;
  --office-b:#0e1a2c;
  --ember-a:#8a1330;
  --ember-b:#120608;
}
*{margin:0;padding:0;box-sizing:border-box}
html,body{width:1200px;height:767px;overflow:hidden;background:var(--stage)}
body{font-family:'Montserrat',Arial,sans-serif;color:var(--ink);position:relative}
.page{position:absolute;width:250px;height:354px;background:var(--white);overflow:hidden;box-shadow:0 2px 6px rgba(0,0,0,.18)}
.page--back{left:330px;top:20px}
.page--front{left:620px;top:20px}
.page--intro{left:330px;top:393px}
.page--features{left:620px;top:393px}
.block{position:absolute}
.photo-ember{background:linear-gradient(100deg,var(--ember-b) 10%,var(--ember-a) 55%,#3a0a14 100%)}
.photo-office{background:linear-gradient(160deg,#6f8fb8 0%,var(--office-a) 40%,var(--office-b) 100%)}
.photo-desk{background:linear-gradient(120deg,#111 20%,#3d3535 60%,#6b5d58 100%)}
.photo-coast{background:linear-gradient(180deg,#c4c7cb 0%,#8e949b 60%,#5e6267 100%)}
.photo-meeting{background:linear-gradient(140deg,#2a2a2e 0%,#43403f 50%,#151517 100%)}
.photo-portrait{background:linear-gradient(170deg,#b9bec4 0%,#7b828c 45%,#4b5360 100%)}
.fill-red{background:var(--red)}
.fill-black{background:var(--black)}
.fill-white{background:var(--white)}

.cta{color:var(--white);padding:17px 0 0 23px}
.cta__label{font-size:6px;letter-spacing:.3px}
.cta__phone{font-size:11px;font-weight:400;margin:3px 0 6px}
.cta__line{font-size:5px;line-height:7.5px}
.ghost-name{position:absolute;left:0;top:0;width:198px;height:203px;display:flex;align-items:center;justify-content:center;font-size:34px;font-weight:600;color:var(--mist)}

.brand{position:absolute;left:65px;top:0;width:185px;height:76px;display:flex;align-items:center;justify-content:center;font-size:25px;font-weight:500;color:var(--ink)}
.headline{position:absolute;left:65px;top:278px;width:185px;height:76px;padding:15px 0 0 30px;line-height:1}
.headline__strong{font-size:19.5px;font-weight:500;letter-spacing:.2px}
.headline__light{font-size:19.5px;font-weight:300;letter-spacing:.3px}
.headline__small{font-size:9.6px;font-weight:400;margin-top:1px}

.intro{position:absolute;left:52px;top:39px;width:198px;height:150px;text-align:center;padding:7px 10px 0}
.intro__lead{font-size:7.6px;font-weight:500}
.intro__accent{font-size:14px;font-weight:500;color:var(--red);line-height:1}
.intro__title{font-size:13.6px;font-weight:600;line-height:1.05}
.intro__sub{font-size:8px;font-weight:500;margin-bottom:6px}
.intro__ask{font-size:6px;font-weight:500;line-height:7.4px;margin-bottom:5px}
.intro__body{font-size:3.9px;line-height:5.3px}

.features-tab{position:absolute;left:0;top:0;width:124px;height:39px;background:var(--black);color:var(--white);font-size:10.5px;font-weight:600;padding:14px 0 0 17px}
.features-tab span{font-weight:300}
.pitch{position:absolute;left:137px;top:39px;width:100px;height:150px;background:var(--red);color:var(--white);font-size:8.6px;line-height:14.2px;padding:24px 0 0 11px}
.feature-list{position:absolute;left:0;top:189px;width:250px;height:165px}
.feature{position:absolute;left:0;width:250px;height:39px;display:flex}
.feature__label{width:124px;height:100%;background:var(--black);display:flex;align-items:center;padding-left:15px;color:var(--white);font-size:9.6px;line-height:10.5px;font-weight:500}
.feature__icon{width:17px;height:17px;border-radius:50%;background:var(--white);margin-right:10px;flex:none;display:flex;align-items:center;justify-content:center}
.feature__text{flex:1;border-bottom:1px solid var(--red);font-size:4px;line-height:5.2px;padding:8px 12px 0 5px;text-align:justify}
</style>
</head>
<body>

<section class="page page--back" aria-label="Back cover">
  <div class="block photo-ember" style="left:0;top:0;width:198px;height:76px" role="img" aria-label="Camera operator filming in red-lit studio"></div>
  <div class="block fill-red" style="left:198px;top:0;width:52px;height:76px"></div>
  <div class="block fill-white" style="left:0;top:76px;width:198px;height:203px"><div class="ghost-name">quillbarn</div></div>
  <div class="block photo-office" style="left:198px;top:76px;width:52px;height:203px" role="img" aria-label="Glass-walled office interior"></div>
  <div class="block fill-black cta" style="left:0;top:278px;width:126px;height:76px">
    <p class="cta__label">CALL TO ACTION</p>
    <p class="cta__phone">415.555.0187</p>
    <p class="cta__line">NORA@QUILLBARN.CO</p>
    <p class="cta__line">WWW.QUILLBARN.CO</p>
  </div>
  <div class="block photo-desk" style="left:126px;top:278px;width:124px;height:76px" role="img" aria-label="Person working at a laptop with coffee"></div>
</section>

<section class="page page--front" aria-label="Front cover">
  <div class="block fill-red" style="left:0;top:0;width:65px;height:76px"></div>
  <div class="brand">quillbarn</div>
  <div class="block photo-office" style="left:0;top:76px;width:250px;height:202px" role="img" aria-label="Team meeting around a table in a modern office"></div>
  <div class="block photo-desk" style="left:0;top:278px;width:65px;height:76px" role="img" aria-label="Desk detail near a window"></div>
  <div class="headline">
    <p class="headline__strong">STRATEGIC</p>
    <p class="headline__light">BUSINESS</p>
    <p class="headline__small">CONSULTING AGENCY</p>
  </div>
</section>

<section class="page page--intro" aria-label="Inside left page">
  <div class="block photo-ember" style="left:52px;top:0;width:198px;height:39px" role="img" aria-label="Dark red atmospheric photo band"></div>
  <div class="block photo-coast" style="left:0;top:39px;width:52px;height:150px" role="img" aria-label="Seaside promenade with palm trees"></div>
  <div class="intro">
    <p class="intro__lead">IF YOU'RE A</p>
    <p class="intro__accent">DIVORCE</p>
    <p class="intro__title">PROFESSIONAL,</p>
    <p class="intro__sub">YOUR BRAND IS YOU</p>
    <p class="intro__ask">MAYBE IT'S TIME TO START PAYING<br>ATTENTION TO WHAT THAT MEANS.</p>
    <p class="intro__body">AS WITH ANY DIVORCE PROFESSIONAL, YOUR BRAND IS YOU. IT'S NOT YOUR LOGO, LETTERHEAD, OR THOSE FANCY WATER BOTTLES YOU GIVE AWAY EVERY YEAR. IT IS EVERYTHING YOUR MARKET KNOWS, OR BELIEVES THEY KNOW, ABOUT HOW YOU CHOOSE TO PRACTICE AND THE RESULTS YOU ACHIEVE. IT DOES NOT DIFFERENTIATE BETWEEN FACT AND EMOTION, IT IS SIMPLY THE PERCEPTION OF YOUR OFFERING THAT EXISTS IN THE MINDS OF THE PEOPLE WHO CHOOSE (OR DON'T CHOOSE) YOU TO WORK WITH THEM.</p>
  </div>
  <div class="block photo-meeting" style="left:52px;top:189px;width:198px;height:116px" role="img" aria-label="Presenter leading a workshop with laptops"></div>
  <div class="block fill-red" style="left:0;top:305px;width:52px;height:38px"></div>
  <div class="block fill-black" style="left:0;top:343px;width:250px;height:11px"></div>
</section>

<section class="page page--features" aria-label="Inside right page">
  <div class="features-tab"><span>OUR</span>FEATURES</div>
  <div class="block photo-portrait" style="left:0;top:39px;width:250px;height:150px" role="img" aria-label="Young man on a phone call on a balcony by the sea"></div>
  <div class="pitch">WE OFFER FULL<br>SERVICE<br>REPRESENTATIO<br>N TO GIVE YOU<br>FREEDOM TO DO<br>THE WORK YOU<br>NEED TO DO.</div>
  <div class="feature-list">
    <div class="feature" style="top:0">
      <div class="feature__label"><span class="feature__icon"><svg width="11" height="11" viewBox="0 0 11 11"><text x="5.5" y="9" font-family="Montserrat,Arial,sans-serif" font-size="10" font-weight="600" text-anchor="middle" fill="#0c0c0d">$</text></svg></span>FLAT FEE</div>
      <p class="feature__text">WITH OUR REPRESENTATION PLATFORM, YOU PAY ONE FEE THAT COVERS YOU FOR ALL STANDARD SERVICES.</p>
    </div>
    <div class="feature" style="top:39px">
      <div class="feature__label"><span class="feature__icon"><svg width="11" height="11" viewBox="0 0 11 11"><rect x="3" y="1" width="5" height="9" rx="1" fill="none" stroke="#0c0c0d" stroke-width="1.1"/><line x1="4.8" y1="8.6" x2="6.2" y2="8.6" stroke="#0c0c0d" stroke-width=".8"/></svg></span>FRIENDLY<br>SUPPORT</div>
      <p class="feature__text">YOUR ACCOUNT MANAGER AND SUPPORT TEAM IS ALWAYS AVAILABLE TO ENSURE THINGS RUN SMOOTHLY.</p>
    </div>
    <div class="feature" style="top:78px">
      <div class="feature__label"><span class="feature__icon"><svg width="11" height="11" viewBox="0 0 11 11"><path d="M2 9 L2.5 7 L7.5 2 L9 3.5 L4 8.5 Z" fill="none" stroke="#0c0c0d" stroke-width="1"/></svg></span>CUSTOMIZED<br>ITEMS</div>
      <p class="feature__text">ALL CLIENTS UNDER REPRESENTATION CAN SUBMIT REQUESTS FOR SPECIFIC CUSTOM MARKETING OR ADVERTISING OPPORTUNITIES.</p>
    </div>
    <div class="feature" style="top:117px;height:48px">
      <div class="feature__label"><span class="feature__icon"><svg width="11" height="11" viewBox="0 0 11 11"><path d="M1.5 5.5 L5.5 1.5 L9.5 1.5 L9.5 5.5 L5.5 9.5 Z" fill="none" stroke="#0c0c0d" stroke-width="1"/><circle cx="7.6" cy="3.4" r=".8" fill="#0c0c0d"/></svg></span>EXCLUSIVE<br>PLATFORM</div>
      <p class="feature__text" style="border-bottom:3px solid var(--red);padding-top:6px">WE DON'T REPRESENT ANYONE WHO WANTS IT. YOU CAN BE ASSURED THAT EVERYONE IN OUR CIRCLE HAS BEEN HAND SELECTED AND SCREENED FOR AUTHENTICITY AND QUALITY OF SERVICE.</p>
    </div>
  </div>
</section>

</body>
</html>
```